Web Design Project (Renewable Energy Services Company)

Hello crowd,

We are looking to create a website for a new company. We would like to have the page already coded, if you do not provide the code as well, please indicate so. I am including a very preliminary approximation of the wireframe.

We do not have the logo either the color pallet, however we have in mind couple websites that would be similar tho these.

http://www.brivolen.com/en/

and

http://www.tarmuvex.com/

We did an approximated wireframe our our website, not necesarly to decide on the layout but rather to know how many pages will be needed. It would be around 10 pages. We will need a section that will be an e-commerce page to sell products such as engineering instrumentation, software and consumables such as cable and connectors.

Our company will be called ORVIK. We will be based in Monterrey, Mexico. Our focused will be the development of renewable energy projects. Similar scope of services than http://www.brivolen.com/en/ but only for wind and solar projects.

We like something minimalistic. Some of the things that the logo might or might not include would be the monterrey famous hill, but not strictly necessary.
http://en.plavorinet.org/wiki/Loma_del_Trueno

also ORVIK (which stands for ORganica VIKtoria) the name is similar the bird (seagal) or wind turbines and sun...any of these are only suggestions and we are open to receive any proposals.

There must be a
home page
services page (some subsections)
products page (some subsections)
contact page with contact form

and some additional subsections like careers and partnerships.

We are very excited to start hearing about this project.
Updates

Please for the logo, do not restrict your ideas to the ones provided as it has generated too specific logos. Pleae just allow your imagination to flow for a company that develops renewable energy projects.

Target Market(s)

large companies interested in developing renewable energy projects

Industry/Entity Type

E-Commerce

Requirements
Must have
• Minimalistic and unique design.
Nice to have
• contact form to save contacts in a database

Should not have
• We are looking a very minimalistic logo. It should not be an explicit wind turbine a seagal or anything like that. we are looking for abstract, simple and minimalistic image.

```html
<!DOCTYPE html>
<html lang="es">
<head>
<meta charset="utf-8">
<title>ORVIK — Proyectos Renovables</title>
<link rel="stylesheet" href="https://fonts.googleapis.com/css2?family=Ubuntu:wght@400;500;700&family=Open+Sans:wght@400;600;700&display=swap">
<style>
  :root {
    --green: #7cb518;
    --green-dark: #5e9410;
    --green-light: #9fd131;
    --page: #ebebeb;
    --panel: #f5f5f5;
    --text: #333333;
    --nav-text: #6a6a6a;
    --heading-grey: #555555;
    --footer: #262626;
    --footer-bottom: #1d1d1d;
    --footer-text: #cfcfcf;
    --dot: #bdbdbd;
  }
  * { box-sizing: border-box; margin: 0; padding: 0; }
  html, body { width: 1200px; height: 928px; overflow: hidden; }
  body {
    position: relative;
    background: var(--page);
    font-family: "Open Sans", sans-serif;
    color: var(--text);
  }
  .top-rule { position: absolute; left: 0; top: 0; width: 1200px; height: 4px; background: var(--green); }

  .brand { position: absolute; left: 109px; top: 30px; display: flex; align-items: center; gap: 14px; }
  .brand-mark { width: 70px; height: 70px; border-radius: 50%; background: var(--green); }
  .brand-name { font-family: "Ubuntu", sans-serif; font-weight: 700; font-size: 50px; color: var(--green); letter-spacing: 1px; }

  .cart { position: absolute; left: 770px; top: 24px; display: flex; align-items: center; gap: 8px; font-family: "Ubuntu", sans-serif; font-size: 11.5px; color: #333; }
  .cart a { color: var(--green); font-weight: 500; text-decoration: none; margin-left: 4px; }
  .search-tab { position: absolute; left: 1041px; top: 0; width: 24px; height: 55px; }

  .search { position: absolute; left: 800px; top: 90px; width: 258px; height: 40px; }
  .search-field {
    position: absolute; left: 0; top: 2px; width: 215px; height: 34px;
    border-radius: 17px; background: #f7f7f7; border: 1px solid #dcdcdc;
    font-family: "Open Sans", sans-serif; font-size: 11.5px; color: #555;
    padding: 9px 0 0 18px;
  }
  .search-go {
    position: absolute; left: 206px; top: 0; width: 52px; height: 40px;
    background: linear-gradient(#9fd131, #5e9410); border-radius: 3px;
    color: #fff; font-family: "Ubuntu", sans-serif; font-weight: 700; font-size: 20px;
    display: flex; align-items: center; justify-content: center;
  }

  .main-nav { position: absolute; left: 111px; top: 167px; height: 37px; display: flex; align-items: center; font-family: "Ubuntu", sans-serif; font-weight: 700; font-size: 14.5px; color: var(--nav-text); }
  .main-nav span { position: absolute; top: 10px; white-space: nowrap; }
  .main-nav .active {
    top: 0; left: 0; width: 105px; height: 37px; border-radius: 5px;
    background: linear-gradient(#9fd131, #6aa312); color: #fff;
    display: flex; align-items: center; justify-content: center;
  }
  .nav-sep { position: absolute; top: 0; width: 1px; height: 40px; background: linear-gradient(transparent, #d0d0d0, transparent); }

  .hero-art {
    position: absolute; left: 100px; top: 268px; width: 455px; height: 380px;
    background: radial-gradient(circle at 30% 55%, #2a4bb0 0%, #3a66d8 35%, #c9ccd2 70%, transparent 78%);
  }
  .slider-dots { position: absolute; left: 412px; top: 650px; display: flex; gap: 10px; }
  .slider-dots i { width: 20px; height: 20px; border-radius: 50%; background: var(--dot); border: 2px solid #f3f3f3; box-shadow: 0 0 2px #999; }
  .slider-dots i.on { background: var(--green); }

  .feature { position: absolute; left: 574px; top: 261px; width: 511px; height: 408px; background: var(--panel); border: 1px solid #fff; box-shadow: 0 0 2px #d8d8d8; }
  .feature h1 { position: absolute; left: 25px; top: 18px; font-family: "Ubuntu", sans-serif; font-weight: 700; font-size: 29px; line-height: 36px; color: var(--heading-grey); }
  .feature h1 .accent { color: var(--green); }
  .feature ul { position: absolute; left: 28px; top: 103px; list-style: none; font-size: 12.5px; line-height: 24px; color: #333; }
  .feature li.title { font-weight: 700; }
  .feature-art {
    position: absolute; left: 305px; top: 150px; width: 200px; height: 250px;
    background: radial-gradient(ellipse at 65% 72%, #f2efe6 0%, #cfd3c8 35%, rgba(220,220,220,0) 70%);
  }

  .tabs { position: absolute; right: 121px; top: 718px; font-family: "Open Sans", sans-serif; font-size: 14px; color: #333; display: flex; gap: 18px; }
  .tabs .on { color: var(--green); text-decoration: underline; }

  .footer { position: absolute; left: 0; top: 769px; width: 1200px; height: 120px; background: var(--footer); }
  .footer-about { position: absolute; left: 111px; top: 20px; width: 620px; font-size: 11px; line-height: 20px; color: var(--footer-text); }
  .contact-head { position: absolute; left: 798px; top: 7px; display: flex; align-items: center; gap: 8px; font-family: "Ubuntu", sans-serif; font-weight: 700; font-size: 21px; }
  .contact-head .icon { width: 38px; height: 38px; border-radius: 4px; background: linear-gradient(#4a4a4a, #1a1a1a); border: 1px solid #555; display: flex; align-items: center; justify-content: center; }
  .contact-head .accent { color: var(--green); }
  .contact-head .plain { color: #fff; }
  .contact-rule { position: absolute; left: 800px; top: 42px; width: 300px; border-top: 1px dotted #555; }
  .contact-address { position: absolute; left: 831px; top: 60px; font-size: 14.5px; line-height: 24px; color: #e8e8e8; font-style: normal; }

  .footer-bar { position: absolute; left: 0; top: 889px; width: 1200px; height: 39px; background: var(--footer-bottom); border-top: 1px dotted #444; }
  .footer-links { position: absolute; left: 127px; top: 15px; font-family: "Open Sans", sans-serif; font-size: 12px; color: #bbb; }
  .footer-links .on { color: var(--green); }
  .footer-links .bar { margin: 0 10px; }
  .copyright { position: absolute; right: 120px; top: 13px; font-size: 14px; color: #e6e6e6; }
</style>
</head>
<body>
  <div class="top-rule"></div>

  <header>
    <div class="brand"><span class="brand-mark"></span><span class="brand-name">ORVIK</span></div>

    <div class="cart">
      <svg width="30" height="24" viewBox="0 0 30 24" aria-hidden="true">
        <path d="M1 3h5l4 13h15l3-10H8" fill="none" stroke="#777" stroke-width="2"/>
        <circle cx="12" cy="20" r="2" fill="#777"/><circle cx="23" cy="20" r="2" fill="#777"/>
      </svg>
      <span>You have no item in your Cart</span><a href="#">Checkout »</a>
    </div>

    <svg class="search-tab" viewBox="0 0 24 55" aria-hidden="true">
      <path d="M0 0h24v48l-12 7-12-7z" fill="#7cb518"/>
      <circle cx="11" cy="33" r="4" fill="none" stroke="#3f6a08" stroke-width="2"/>
      <path d="M14 36l4 4" stroke="#3f6a08" stroke-width="2.5"/>
    </svg>

    <form class="search">
      <div class="search-field">----Search your keyword ----</div>
      <div class="search-go">Go</div>
    </form>

    <nav class="main-nav">
      <span class="active">INICIO</span>
      <i class="nav-sep" style="left:136px"></i>
      <span style="left:166px">SERVICIOS</span>
      <i class="nav-sep" style="left:281px"></i>
      <span style="left:322px">PRODUCTOS</span>
      <i class="nav-sep" style="left:457px"></i>
      <span style="left:500px">NUESTRA</span>
      <i class="nav-sep" style="left:606px"></i>
      <span style="left:647px">ESPECIALIDAD</span>
      <i class="nav-sep" style="left:785px"></i>
      <span style="left:820px">CONTACTO</span>
    </nav>
  </header>

  <main>
    <div class="hero-art" role="img" aria-label="Globo terráqueo con panel solar y aerogenerador"></div>
    <div class="slider-dots"><i class="on"></i><i></i><i></i><i></i><i></i></div>

    <section class="feature">
      <h1><span class="accent">Proyectos Renovables</span><br>para México y Latino América</h1>
      <ul>
        <li class="title">Energía Eólica</li>
        <li>Proyectos de Generación Eólica desde 1MW</li>
        <li>hasta 200MW</li>
        <li>Análisis Detallado de Recurso Eólico</li>
        <li>Diseño de Parques Eólicos</li>
        <li>Permitología</li>
        <li>Comisión Nacional de Red Eléctrica CNRE</li>
        <li>SEPRAMAT</li>
        <li>CRN</li>
        <li>Análisis de Riesgo y Factibilidad Financiera</li>
        <li>PPA and Tariff Analysis</li>
      </ul>
      <div class="feature-art" role="img" aria-label="Casa con panel solar en el techo y aerogenerador"></div>
    </section>

    <div class="tabs"><span class="on">Energía Eólica</span><span>|</span><span>Energía Solar</span></div>
  </main>

  <footer>
    <div class="footer">
      <p class="footer-about">Lorem Ipsum is simply dummy text of the printing and typesetting industry. Lorem Ipsum has been the industry's standard dummy text ever since the 1500s, when an unknown printer took a galley of type and scrambled it to make a type specimen book. It has survived not only five centuries, but also the leap into electronic typesetting, remaining essentially unchanged. It was popularised in the 1960.</p>
      <div class="contact-head">
        <span class="icon">
          <svg width="22" height="22" viewBox="0 0 22 22" aria-hidden="true">
            <path d="M6 3c-2 1-3 3-2 6 2 5 5 8 10 10 3 1 5 0 6-2l-3-3-3 2c-3-1-5-4-6-6l2-3z" fill="#e0a84a"/>
          </svg>
        </span>
        <span><span class="accent">Contact</span> <span class="plain">info:</span></span>
      </div>
      <div class="contact-rule"></div>
      <address class="contact-address">Almendros 215, Col. Valle Los Cedros,<br>Monterrey, N.L. 64870</address>
    </div>
    <div class="footer-bar">
      <div class="footer-links"><span class="on">Carreras</span><span class="bar">|</span><span>Quienes Somos</span></div>
      <div class="copyright">ORVIK S.A. de C.V. ©</div>
    </div>
  </footer>
</body>
</html>
```